Create a beautiful brochure for a Permanent Make Up Clinic

I need a classy brochure for my Permanent Make up Clinic. It needs a classy cover and the list of services and extra information on the inside. I don't have any requirements on size of the brochure, but it needs to look attractive and upmarket. The colors I like are black -white - Gold - grey. I like a minimalistic look.
I’d like to have my logo on the cover, the price list on the inside and the address information at the back.

Target Market(s)

woman between 18 and 99 years old

Industry/Entity Type

Beauty

Font styles to use
Sans Serif
Script

Colors

Designer to choose colors to be used in the design.

Requirements
Must have
• the logo on the cover
• pictures of the services with an explanation and pricing
• address information at the back
Nice to have
• a classy upmarket look, not with too many different colors in it.

```html
<!DOCTYPE html>
<html lang="nl">
<head>
<meta charset="utf-8">
<title>Lumé Studio – Brochure</title>
<link href="https://fonts.googleapis.com/css2?family=Didact+Gothic&family=Roboto+Condensed:wght@300;400&display=swap" rel="stylesheet">
<style>
  :root{
    --stage:#2f3939;
    --paper:#ffffff;
    --ink:#1f2328;
    --ink-soft:#4a5058;
    --band:#343c47;
    --gold:#c39a3c;
    --line:#c9ccd0;
    --body:'Didact Gothic', sans-serif;
    --head:'Roboto Condensed', sans-serif;
  }
  *{box-sizing:border-box;margin:0;padding:0}
  html,body{width:1014px;height:1200px;overflow:hidden;background:var(--stage)}
  .spread{position:absolute;left:37px;top:264px;width:940px;height:671px;display:flex;box-shadow:0 18px 40px rgba(0,0,0,.45)}
  .page{position:relative;width:470px;height:671px;overflow:hidden}
  .back{background:var(--paper);font-family:var(--body);color:var(--ink)}
  .cover{font-family:var(--body);color:#fff}
  .page svg.art{position:absolute;inset:0}

  .intro-text{position:absolute;left:216px;top:282px;width:230px;color:#fff;font-size:9px;line-height:1.22;text-align:justify}
  .intro-text p+p{margin-top:10px}

  .brand{position:absolute;left:0;width:100%;text-align:center}
  .brand-name{font-family:var(--body);font-size:30px;letter-spacing:2px;line-height:1}
  .brand-line{font-size:7.5px;letter-spacing:.8px;margin-top:12px}
  .back .brand{top:470px;color:var(--ink)}
  .back .brand-line{color:var(--ink-soft)}

  .divider{position:absolute;left:30px;top:549px;width:410px;height:1px;background:linear-gradient(90deg,transparent,var(--line) 15%,var(--line) 85%,transparent)}
  .questions{position:absolute;left:29px;top:560px;font-family:var(--head);font-weight:300;font-size:17px;color:var(--ink-soft)}
  .contact{position:absolute;font-size:8.5px;line-height:1.4;color:var(--ink)}
  .contact-left{left:29px;top:600px}
  .contact-right{left:276px;top:580px}
  .contact-right strong{font-weight:400;letter-spacing:.4px;font-family:var(--head);font-size:10px}
  .row{display:flex;align-items:center;gap:4px}
  .row+.row{margin-top:2px}
  .gap{margin-top:12px!important}
  .ico{display:inline-block;width:9px;height:9px;flex:none}
  .ico-dot{border:1px solid var(--ink);border-radius:50%}
  .ico-sq{border:1px solid var(--ink);border-radius:1px}
  .web{position:absolute;left:276px;top:648px;font-size:8.5px}

  .cover .brand{top:34px;color:#fff}
  .cover .brand-line{color:#e6e8ea}
  .headline{position:absolute;left:32px;top:566px;font-family:var(--head);font-weight:300;font-size:22px;line-height:1.3;letter-spacing:-.2px}
  .site{position:absolute;left:32px;top:637px;font-size:8px;letter-spacing:5px;color:#d5d8db}
</style>
</head>
<body>
<main class="spread">

  <section class="page back">
    <svg class="art" width="470" height="671" viewBox="0 0 470 671">
      <defs>
        <linearGradient id="goldRing" x1="0" y1="0" x2="1" y2="1">
          <stop offset="0" stop-color="#8f6a1f"/><stop offset=".45" stop-color="#ecd38a"/><stop offset="1" stop-color="#a57b28"/>
        </linearGradient>
        <linearGradient id="photoWarm" x1="0" y1="0" x2="1" y2="1">
          <stop offset="0" stop-color="#e9e4e0"/><stop offset=".55" stop-color="#c89f86"/><stop offset="1" stop-color="#f1efed"/>
        </linearGradient>
        <linearGradient id="photoPortrait" x1="0" y1="0" x2="0" y2="1">
          <stop offset="0" stop-color="#e9e2c8"/><stop offset="1" stop-color="#d9b39a"/>
        </linearGradient>
        <clipPath id="topClip"><circle cx="200" cy="190" r="152"/></clipPath>
        <clipPath id="aboveBand"><rect x="0" y="0" width="470" height="274"/></clipPath>
      </defs>
      <g clip-path="url(#aboveBand)">
        <circle cx="200" cy="190" r="158" fill="none" stroke="url(#goldRing)" stroke-width="4"/>
        <rect x="40" y="30" width="320" height="244" fill="url(#photoWarm)" clip-path="url(#topClip)" role="img" aria-label="Foto: behandeling van wenkbrauwen met permanente make-up"/>
      </g>
      <rect x="0" y="274" width="470" height="124" fill="#343c47"/>
      <circle cx="110" cy="333" r="93" fill="none" stroke="#9aa0a6" stroke-width=".8"/>
      <circle cx="110" cy="333" r="82" fill="url(#photoPortrait)" role="img" aria-label="Portretfoto van de specialiste"/>
    </svg>
    <div class="intro-text">
      <p>De Permanente Make Up wordt persoonlijk door Sofie Verlinden gezet. Sofie werd opgeleid en blijft zich permanent bijscholen door internationale experten.</p>
      <p>Geen slechte verrassingen bij Lumé Studio! Voor elke behandeling tekenen we altijd een schets, zodat u mee kunt zien welke vorm of kleur het eindresultaat zal hebben.</p>
    </div>

    <div class="brand">
      <div class="brand-name">Lumé Studio</div>
      <div class="brand-line">PERMANENT MAKE UP BY SOFIE VERLINDEN</div>
    </div>

    <div class="divider"></div>
    <h2 class="questions">HEB JE NOG VRAGEN?</h2>
    <div class="contact contact-left">
      <div class="row">
        <svg class="ico" viewBox="0 0 10 10"><circle cx="5" cy="5" r="4.5" fill="none" stroke="#1f2328" stroke-width=".8"/><path d="M3.3 2.8c.4-.3.7-.2.9.2l.4.8c.1.3 0 .5-.2.6l-.2.2c.3.7.8 1.2 1.4 1.5l.2-.2c.2-.2.4-.3.6-.1l.8.4c.4.2.4.5.1.9-.6.7-1.6.4-2.6-.6S2.6 3.4 3.3 2.8z" fill="#1f2328"/></svg>
        <span>Tel</span><span class="ico ico-dot"></span><span>Chat</span>
      </div>
      <div class="row" style="padding-left:13px">+32470118845</div>
      <div class="row gap"><span class="ico ico-sq"></span><span>Socials</span><span class="ico ico-sq" style="margin-left:4px"></span><span>Foto's: @lumestudio</span></div>
    </div>
    <div class="contact contact-right">
      <strong>ENKEL OP AFSPRAAK</strong><br>
      Lumé Studio<br>
      Lindelaan 27 9800<br>
      DEINZE
    </div>
    <div class="contact web row"><span class="ico ico-dot"></span><span>www.lumestudio.be</span></div>
  </section>

  <section class="page cover">
    <svg class="art" width="470" height="671" viewBox="0 0 470 671">
      <defs>
        <linearGradient id="coverBg" x1="0" y1="0" x2="1" y2="0">
          <stop offset="0" stop-color="#2c343c"/><stop offset=".55" stop-color="#6f7a83"/><stop offset="1" stop-color="#5b6770"/>
        </linearGradient>
        <linearGradient id="coverBlue" x1="0" y1="0" x2="1" y2="1">
          <stop offset="0" stop-color="#3d5876"/><stop offset="1" stop-color="#223a58"/>
        </linearGradient>
        <linearGradient id="goldArc" x1="0" y1="0" x2="0" y2="1">
          <stop offset="0" stop-color="#f0d78e"/><stop offset=".5" stop-color="#a87c27"/><stop offset="1" stop-color="#e8c878"/>
        </linearGradient>
        <linearGradient id="photoClinic" x1="0" y1="0" x2="1" y2="1">
          <stop offset="0" stop-color="#c8c2b8"/><stop offset=".5" stop-color="#d9a9c4"/><stop offset="1" stop-color="#8f7a76"/>
        </linearGradient>
        <clipPath id="pageClip"><rect width="470" height="671"/></clipPath>
      </defs>
      <g clip-path="url(#pageClip)">
        <rect width="470" height="671" fill="url(#coverBg)"/>
        <circle cx="520" cy="370" r="355" fill="url(#coverBlue)"/>
        <circle cx="520" cy="370" r="355" fill="none" stroke="url(#goldArc)" stroke-width="4"/>
        <circle cx="520" cy="360" r="250" fill="none" stroke="#e9edf1" stroke-width="1"/>
        <circle cx="520" cy="360" r="215" fill="none" stroke="#9fb0c2" stroke-width=".6"/>
        <circle cx="232" cy="351" r="203" fill="none" stroke="url(#goldArc)" stroke-width="3.5" stroke-dasharray="640 1000" transform="rotate(95 232 351)"/>
        <circle cx="232" cy="351" r="200" fill="url(#photoClinic)" role="img" aria-label="Foto: specialiste met roze handschoenen zet permanente make-up bij de ogen"/>
      </g>
    </svg>
    <div class="brand">
      <div class="brand-name">Lumé Studio</div>
      <div class="brand-line">PERMANENT MAKE UP BY SOFIE VERLINDEN</div>
    </div>
    <h1 class="headline">BENADRUK JE<br>NATUURLIJKE SCHOONHEID!</h1>
    <div class="site">www.lumestudio.be</div>
  </section>

</main>
</body>
</html>
```